FLUSH FAIRY the solution to twinkle the smell away...because everyone poops

I need a label for my handmade poop spray. Flush fairy is an organic blend of essential oils that eliminates the odor when you poop. Directions must be on the back of the label : shake well before each use. Spray on the toilet water surface 4-6 times to cover the water before you go. Poop as usual and flush. Safe for all pipes and sewer systems. To order visit my Vendly shop enter flush fairy

Font styles to use
Decorative

Requirements
Must have
• Directions on how to use
Nice to have
• Elegant design label. Product is meant to be kept in the bathroom

```html
<!DOCTYPE html>
<html lang="en">
<head>
<meta charset="utf-8">
<title>Flush Fairy – Handmade Poop Spray Label</title>
<link rel="stylesheet" href="https://fonts.googleapis.com/css2?family=Pinyon+Script&family=Yesteryear&family=Open+Sans:ital,wght@0,400;0,700;1,700&display=swap">
<style>
  :root {
    --page: #ececec;
    --label-white: #ffffff;
    --band-green: #5aa333;
    --leaf-green: #7cc142;
    --lime: #c8e04a;
    --deep-green: #2f6f1c;
    --badge-green: #3f8a2a;
    --badge-text: #f2f56a;
    --band-text: #eef6e6;
    --ink: #2b2b2b;
  }
  html, body {
    margin: 0;
    padding: 0;
    width: 1200px;
    height: 1200px;
    overflow: hidden;
    background: var(--page);
    font-family: "Open Sans", sans-serif;
  }
  .label {
    position: absolute;
    left: 50px;
    top: 275px;
    width: 1100px;
    height: 650px;
    display: flex;
    background: var(--label-white);
    box-shadow: 0 2px 10px rgba(0,0,0,0.12);
  }
  .band {
    background: var(--band-green);
    color: var(--band-text);
    display: flex;
    align-items: center;
    justify-content: center;
  }
  .band-left { width: 180px; }
  .band-right { width: 258px; }
  .band-text {
    writing-mode: vertical-rl;
    transform: rotate(180deg);
    height: 600px;
    font-size: 19px;
    line-height: 1.45;
  }
  .ingredients-text { display: flex; gap: 34px; justify-content: flex-start; padding-top: 10px; }
  .directions { margin: 0; padding: 0; list-style: none; font-size: 20px; }
  .directions li::before { content: "\25CF\00a0"; }
  .directions .safe { font-weight: 700; }
  .front-panel {
    position: relative;
    flex: 1;
    overflow: hidden;
  }
  .splash-art {
    position: absolute;
    inset: 40px 20px 70px 20px;
    border-radius: 40% 40% 45% 45%;
    background: radial-gradient(ellipse at 50% 52%, #f6fbec 0%, #e2f1c4 35%, var(--leaf-green) 75%, var(--lime) 100%);
    opacity: 0.9;
  }
  .top-banner {
    position: absolute;
    top: 36px;
    left: 50%;
    transform: translateX(-50%);
    width: 420px;
    height: 36px;
    border-radius: 50%;
    background: var(--leaf-green);
    color: var(--badge-text);
    font-weight: 700;
    font-style: italic;
    font-size: 16px;
    letter-spacing: 2px;
    display: flex;
    align-items: center;
    justify-content: center;
  }
  .product-name {
    position: absolute;
    top: 220px;
    width: 100%;
    text-align: center;
    font-family: "Pinyon Script", cursive;
    font-size: 112px;
    line-height: 1;
    color: var(--deep-green);
    margin: 0;
    font-weight: 400;
  }
  .blend-badge {
    position: absolute;
    top: 382px;
    left: 50%;
    transform: translateX(-50%);
    padding: 6px 38px;
    background: var(--badge-green);
    border: 3px solid #ffffff;
    border-radius: 16px;
    font-family: "Yesteryear", cursive;
    font-size: 34px;
    color: var(--badge-text);
    white-space: nowrap;
  }
  .volume {
    position: absolute;
    bottom: 22px;
    width: 100%;
    text-align: center;
    font-weight: 700;
    font-size: 20px;
    color: var(--ink);
  }
</style>
</head>
<body>
  <main class="label">
    <aside class="band band-left">
      <div class="band-text ingredients-text">
        <span>Ingredients: ....... ...............</span>
        <span>order visit my Vendly shop enter flush fairy</span>
      </div>
    </aside>

    <section class="front-panel">
      <div class="splash-art" role="img" aria-label="Decorative green and lime leaf-shaped splashes around a large star outline"></div>
      <div class="top-banner">HANDMADE POOP SPRAY</div>
      <h1 class="product-name">Flush Fairy</h1>
      <div class="blend-badge">Organic Blend</div>
      <div class="volume">115 ml</div>
    </section>

    <aside class="band band-right">
      <ul class="band-text directions">
        <li>Shake well before each use</li>
        <li>Spray on the toilet water surface 4-6 times to cover the water before you go</li>
        <li>Poop as usual and flush.</li>
        <li class="safe">Safe for all pipes and sewer systems.</li>
      </ul>
    </aside>
  </main>
</body>
</html>
```